Infectious Diseases Research Laboratory Needs Business Card

We need a business card for an academic research laboratory based in Kansas City called MORVEK. The full lab name is Microbial Dose-Response/Exposure Bridging Studies Laboratory, but this does not need to be incorporated. We study novel ways to optimize the treatment of multidrug-resistant bacterial infections ("superbugs") throughout the entire biomedical research spectrum (from benchtop to bedside). The name MORVEK is not only an acronym for our lab name, but also represents our desire to make discoveries and explore the unknown (the stars, if you well). It also serves as an ode to the state of Kansas motto where we are based, ad astra per aspera ("to the stars, through difficulty").

Target Market(s)

Pharmaceutical companies, researchers

Industry/Entity Type

Pharmaceutical

Contact Information for Business Card

The business card should incorporate and complement our new logo (see uploaded files). Double-sided designs are preferred. Looking for something modern, but professional.

Font styles to use
Sans Serif

Requirements
Must have
• Double-sided. One side would ideally be a solid color incorporating logo and the other should also have the logo (smaller), but incorporate staff information.
• Color codes:
• Red: #F04C51
• Blue: #3477B5
• Gray: #808285

```html
<!DOCTYPE html>
<html lang="en">
<head>
<meta charset="utf-8">
<title>MORVEK Business Card</title>
<link rel="stylesheet" href="https://fonts.googleapis.com/css2?family=Roboto:wght@300;400;700&display=swap">
<style>
  :root {
    --red: #F04C51;
    --blue: #3477B5;
    --gray: #808285;
    --charcoal: #2c2c2e;
    --paper: #ececee;
    --backdrop: #5a5b5e;
    --ink: #1f1f21;
  }
  * { margin: 0; padding: 0; box-sizing: border-box; }
  html, body {
    width: 1200px; height: 1200px; overflow: hidden;
    background: var(--backdrop);
    font-family: "Roboto", Arial, sans-serif;
  }
  .canvas { position: relative; width: 1200px; height: 1200px; }
  .card {
    position: absolute; left: 160px; width: 880px; height: 503px;
    overflow: hidden; background: var(--charcoal);
    box-shadow: 0 14px 30px rgba(0,0,0,.35);
  }
  .card--back { top: 60px; }
  .card--front { top: 637px; }

  /* brand mark */
  .brand { display: flex; align-items: center; gap: 18px; }
  .brand__dot { width: 40px; height: 40px; border-radius: 50%; background: var(--blue); }
  .brand__name {
    color: var(--red); font-weight: 300; letter-spacing: 10px; line-height: 1;
  }

  /* back side */
  .back__top-band {
    position: absolute; left: 130px; top: 0; width: 500px; height: 16px;
    background: var(--red); border-radius: 0 0 14px 0;
  }
  .card--back .brand {
    position: absolute; left: 50%; top: 50%; transform: translate(-50%, -50%);
  }
  .card--back .brand__name { font-size: 72px; }
  .back__bottom-band {
    position: absolute; left: 0; top: 405px; width: 330px; height: 34px;
    background: var(--gray); border-radius: 0 10px 10px 0;
  }

  /* front side */
  .front__panel {
    position: absolute; left: 0; top: 0; width: 520px; height: 100%;
    background: var(--paper);
  }
  .front__tab {
    position: absolute; left: 370px; top: 0; width: 150px; height: 60px;
    background: var(--red);
  }
  .front__rule {
    position: absolute; left: 360px; top: 100px; width: 160px; height: 6px;
    background: var(--red);
  }
  .staff { position: absolute; left: 48px; top: 72px; }
  .staff__name {
    font-size: 32px; font-weight: 300; color: var(--ink);
    letter-spacing: 0.5px; line-height: 1.15; white-space: nowrap;
  }
  .staff__name b { font-weight: 700; }
  .staff__role { font-size: 18px; color: var(--blue); margin-top: 6px; }
  .contact {
    position: absolute; left: 130px; top: 205px;
    border-left: 4px solid var(--red); padding: 8px 0 8px 30px;
    font-size: 20px; color: var(--ink); line-height: 1.75;
  }
  .address-band {
    position: absolute; left: 0; top: 430px; width: 540px; height: 46px;
    background: var(--red); border-radius: 0 20px 20px 0;
    color: #fff; font-size: 20px; padding-left: 48px;
    display: flex; align-items: center;
  }
  .card--front .brand { position: absolute; left: 585px; top: 180px; gap: 14px; }
  .card--front .brand__dot { width: 28px; height: 28px; }
  .card--front .brand__name { font-size: 44px; letter-spacing: 6px; }
  .front__accent {
    position: absolute; left: 590px; top: 310px; width: 290px; height: 56px;
    background: var(--red); border-radius: 18px 0 0 18px;
  }
  .front__accent::after {
    content: ""; position: absolute; left: 40px; top: 24px; width: 220px; height: 8px;
    background: #fff;
  }
</style>
</head>
<body>
<main class="canvas">
  <section class="card card--back" aria-label="Card back">
    <div class="back__top-band"></div>
    <div class="brand">
      <span class="brand__dot"></span>
      <span class="brand__name">MORVEK</span>
    </div>
    <div class="back__bottom-band"></div>
  </section>

  <section class="card card--front" aria-label="Card front">
    <div class="front__panel"></div>
    <div class="front__tab"></div>
    <div class="front__rule"></div>
    <div class="staff">
      <p class="staff__name"><b>DANA</b> KOVALSKI</p>
      <p class="staff__role">Research Executive</p>
    </div>
    <div class="contact">
      <p>000.555.0142</p>
      <p>info@morvek.com</p>
      <p>www.morvek.com</p>
    </div>
    <div class="address-band">418 Prairie Lane, Kansas City, USA</div>
    <div class="brand">
      <span class="brand__dot"></span>
      <span class="brand__name">MORVEK</span>
    </div>
    <div class="front__accent"></div>
  </section>
</main>
</body>
</html>
```